Varnel Flyer

We need a flyer designed for a Security Company. Our main focus is security consulting and risk management. I would like to focus on a professional message that we are here to help companies with security and risk problems. We are independent and do not affiliate with any other companies.

Who we are:
Over 25+ years of experience in Security and Law Enforcement
Specialize in Security Management
Board Certified in Security management
Accredited defense Specialist (ADS)
We are not affiliated with any security provider or guard company we provide independent advise

Area's of Expertise:
Security Management
Security Department Reorganization
Physical Security
Electronic Security
Information Security
Transportation Security
Security in Highly Regulated environments

Services Offered:

Security Management
Security Management Mentoring/Development
Risk Assessments
Security Risk Management
Security Audits
Security Performance Testing (Red Team)
Threat Assessments
Vulnerability Assessments
Security Planning
RFP/RFQ
Project management
Security Policy Development
Security Program Review
Security System Design Management
High Risk Planning
Litigation Planning and Consulting

What to look for in a Security Consultant:

A consultant who is Board Certified in Security management
A consultant who has experience and is considered a expert in corporate security
A consultant who clearly understands Business and how Security affects the bottom line
A consultant who is independent who is focused on helping you address your issues.
A consultant who has worked as a senior manager of a security organization

Industries:

Energy
Healthcare
Real Estate
Nuclear
Highly secure facilities

Accredited Defense Specialist (ADS)

The Accredited Defense Specialist (ADSⓇ) is considered the “gold standard” certification for security management professionals and demonstrates knowledge and competency in seven key domains of security. Globally recognized as the standard of excellence for security management professionals. The ADS is administered by OPRA Worldwide, which is the predominant international organization for security Internationally.

Contact us:

Phone: 555-271-6043
info@varnelguard.example
www.varnelguard.example

```html
<!DOCTYPE html>
<html lang="en">
<head>
<meta charset="utf-8">
<title>Varnel Services – Trifold Brochure</title>
<link rel="stylesheet" href="https://fonts.googleapis.com/css2?family=Arimo:ital,wght@0,400;0,700;1,400&display=swap">
<style>
:root{
  --bg:#e4e4e4;
  --blue:#1b7fc6;
  --blue-dark:#0f5b98;
  --blue-light:#5fb2ea;
  --charcoal:#3b3c3e;
  --charcoal-dark:#2c2d2f;
  --silver-1:#f4f4f4;
  --silver-2:#c9cacc;
  --navy-1:#0b1a33;
  --navy-2:#27466f;
  --white:#ffffff;
  --ink:#2b2b2b;
  --muted:#d6dbe0;
}
*{box-sizing:border-box;margin:0;padding:0}
html,body{width:1200px;height:2400px;overflow:hidden}
body{background:var(--bg);font-family:"Arimo",Arial,sans-serif;color:var(--white);position:relative}
.spread{position:absolute;left:45px;width:1110px;height:820px;display:flex;box-shadow:0 18px 40px rgba(0,0,0,.22)}
.spread--outside{top:290px}
.spread--inside{top:1290px}
.panel{position:relative;width:370px;height:820px;overflow:hidden}
.photo{position:absolute;left:0;right:0}
ul{list-style:none}

/* ---------- outside: back panel ---------- */
.back{background:var(--charcoal)}
.back .photo{top:0;height:260px;background:linear-gradient(135deg,#c9d3da,#8fa1ae 55%,#5f6f7b)}
.back .band{position:absolute;top:240px;left:0;width:370px;height:60px}
.badge{position:absolute;top:330px;left:40px;display:flex;align-items:center;gap:14px}
.badge__seal{width:62px;height:62px;border-radius:50%;background:var(--white)}
.badge__label{font-size:15px;font-weight:700;line-height:1.2;color:var(--white)}
.back__copy{position:absolute;top:425px;left:40px;right:34px;font-size:13.5px;line-height:1.5;color:var(--muted)}
.back__copy p+p{margin-top:12px}
.back__more{position:absolute;bottom:46px;left:40px;font-size:13px;line-height:1.5;color:var(--muted)}

/* ---------- outside: middle panel ---------- */
.about{background:linear-gradient(180deg,var(--blue) 0%,var(--blue-dark) 100%)}
.about h2,.contact h2{font-size:24px;font-weight:700;text-align:center;letter-spacing:.5px}
.about__intro{position:absolute;top:46px;left:32px;right:30px}
.about__intro ul{margin-top:18px}
.about__intro li{font-size:13.5px;line-height:1.4;padding-left:20px;position:relative;margin-bottom:6px}
.about__intro li::before{content:"";position:absolute;left:2px;top:5px;width:8px;height:8px;border:1.5px solid var(--white);border-radius:50%}
.wordmark{display:flex;align-items:center;gap:12px}
.wordmark__mark{width:44px;height:44px;border:0;background:var(--white)}
.wordmark__name{font-size:32px;font-weight:700;letter-spacing:1px;line-height:1}
.wordmark__tag{font-size:11px;font-weight:400;margin-top:4px;letter-spacing:.3px}
.about .wordmark{position:absolute;top:400px;left:60px}
.contact{position:absolute;top:540px;left:40px;right:30px}
.contact ul{margin-top:22px}
.contact li{display:flex;align-items:center;gap:12px;font-size:15px;margin-bottom:14px}
.contact svg{width:18px;height:18px;flex:none}

/* ---------- outside: cover ---------- */
.cover{background:var(--charcoal)}
.cover__head{position:absolute;top:0;left:0;right:0;height:175px;background:linear-gradient(160deg,var(--silver-1),var(--silver-2));display:flex;align-items:center;justify-content:center}
.cover__head .wordmark__mark{background:var(--blue-dark)}
.cover__head .wordmark__name,.cover__head .wordmark__tag{color:var(--blue-dark)}
.cover .photo{top:175px;height:330px;background:radial-gradient(circle at 55% 45%,#5d8fc9 0%,var(--navy-2) 35%,var(--navy-1) 85%)}
.cover .stripe{position:absolute;top:470px;left:0;width:370px;height:90px}
.cover__title{position:absolute;top:590px;left:34px;right:30px;font-size:25px;line-height:1.25;color:var(--blue-light);text-transform:uppercase;text-align:center}
.cover__url{position:absolute;top:700px;left:34px;right:0;height:44px;background:var(--blue);display:flex;align-items:center;justify-content:center;font-size:19px;font-weight:700;letter-spacing:1.5px}
.cover__cta{position:absolute;top:758px;right:28px;font-size:12px;line-height:1.35;text-align:right;color:var(--muted)}

/* ---------- inside: services ---------- */
.services{background:var(--blue)}
.services h3{position:absolute;top:40px;left:32px;font-size:22px;font-weight:700}
.services ul{position:absolute;left:32px;right:20px}
.services li{font-size:14px;line-height:1.25;padding-left:20px;position:relative;margin-bottom:6px}
.services li::before{content:"";position:absolute;left:0;top:3px;width:10px;height:10px;border-radius:50%;background:var(--white)}
.services .list-a{top:84px}
.services .list-b{top:560px}
.services .photo{top:335px;height:195px;background:linear-gradient(120deg,#0e3562,#2d79b8 55%,#8fc6ec)}
.services .band{position:absolute;top:320px;left:0;width:370px;height:30px}

/* ---------- inside: consultant ---------- */
.consultant{background:var(--white)}
.consultant__head{position:absolute;top:0;left:0;right:0;height:200px;background:var(--charcoal)}
.consultant h3{position:absolute;top:36px;left:20px;right:20px;text-align:center;font-size:21px;line-height:1.25;color:var(--blue-light);text-transform:uppercase}
.consultant__disc{position:absolute;top:130px;left:115px;width:140px;height:140px;border-radius:50%;border:8px solid #e6e8ea;background:radial-gradient(circle,#cfd6dd,#8b99a6)}
.consultant ul{position:absolute;top:305px;left:30px;right:26px}
.consultant li{color:var(--ink);font-size:14px;line-height:1.4;padding-left:24px;position:relative;margin-bottom:14px}
.consultant li svg{position:absolute;left:0;top:3px;width:14px;height:14px}
.consultant__more{position:absolute;bottom:90px;left:36px;right:36px;border:1.5px solid var(--blue);padding:12px 0;text-align:center;font-size:14px;line-height:1.5;color:#666}
.consultant__more strong{color:var(--blue);font-weight:400;display:block;font-size:15px}

/* ---------- inside: expertise ---------- */
.expertise{background:linear-gradient(180deg,var(--blue) 0%,var(--blue-dark) 100%)}
.expertise .photo{top:0;height:250px;background:linear-gradient(150deg,#b9a48c,#8d8a86 50%,#dcdcdc)}
.expertise h3{font-size:21px;font-weight:700;text-transform:uppercase}
.expertise .block{position:absolute;left:34px;right:24px}
.expertise .block--areas{top:290px}
.expertise .block--industries{top:560px}
.expertise ul{margin-top:14px}
.expertise li{font-size:14px;line-height:1.25;padding-left:20px;position:relative;margin-bottom:6px}
.expertise li::before{content:"";position:absolute;left:0;top:3px;width:10px;height:10px;border-radius:50%;background:var(--white)}
</style>
</head>
<body>

<!-- OUTSIDE SPREAD -->
<section class="spread spread--outside">

  <article class="panel back">
    <div class="photo" role="img" aria-label="Photo of a customer support agent wearing a headset"></div>
    <svg class="band" viewBox="0 0 370 60" preserveAspectRatio="none" aria-hidden="true">
      <path d="M0 20 Q185 0 370 14 L370 60 L0 60Z" fill="var(--blue)"/>
      <path d="M0 30 Q185 10 370 24 L370 60 L0 60Z" fill="var(--charcoal)"/>
    </svg>
    <div class="badge">
      <div class="badge__seal"></div>
      <div class="badge__label">Accredited Defense<br>Specialist</div>
    </div>
    <div class="back__copy">
      <p>The Accredited Defense Specialist (ADSⓇ) is considered the “gold standard” certification for security management professionals and demonstrates knowledge and competency in seven key domains of security. Globally recognized as the standard of excellence for security management professionals.</p>
      <p>The ADS is administered by OPRA Worldwide, which is the predominant international organization for security internationally.</p>
    </div>
    <div class="back__more">More details here:<br>www.varnelguard.example</div>
  </article>

  <article class="panel about">
    <div class="about__intro">
      <h2>WHO WE ARE</h2>
      <ul>
        <li>Over 25+ years of experience in Security and Law Enforcement</li>
        <li>Specialize in Security Management</li>
        <li>Board Certified in Security management</li>
        <li>Accredited defense Specialist (ADS)</li>
        <li>We are not affiliated with any security provider or guard company we provide independent advise</li>
      </ul>
    </div>
    <div class="wordmark">
      <div class="wordmark__mark"></div>
      <div>
        <div class="wordmark__name">VARNEL SERVICES</div>
        <div class="wordmark__tag">A Security Management Company</div>
      </div>
    </div>
    <div class="contact">
      <h2>CONTACT US</h2>
      <ul>
        <li><svg viewBox="0 0 24 24" aria-hidden="true"><path fill="#fff" d="M6.6 10.8a15 15 0 0 0 6.6 6.6l2.2-2.2c.3-.3.7-.4 1-.2 1.1.4 2.3.6 3.6.6.6 0 1 .4 1 1V20c0 .6-.4 1-1 1A17 17 0 0 1 3 4c0-.6.4-1 1-1h3.5c.6 0 1 .4 1 1 0 1.3.2 2.5.6 3.6.1.3 0 .7-.2 1z"/></svg>555-271-6043</li>
        <li><svg viewBox="0 0 24 24" aria-hidden="true"><rect x="2" y="5" width="20" height="14" rx="2" fill="#fff"/><path d="M3 6l9 7 9-7" stroke="var(--blue)" stroke-width="2" fill="none"/></svg>info@varnelguard.example</li>
        <li><svg viewBox="0 0 24 24" aria-hidden="true"><circle cx="12" cy="12" r="9" fill="none" stroke="#fff" stroke-width="2"/><path d="M3 12h18M12 3c3 3 3 15 0 18M12 3c-3 3-3 15 0 18" fill="none" stroke="#fff" stroke-width="1.5"/></svg>www.varnelguard.example</li>
      </ul>
    </div>
  </article>

  <article class="panel cover">
    <header class="cover__head">
      <div class="wordmark">
        <div class="wordmark__mark"></div>
        <div>
          <div class="wordmark__name">VARNEL<br>SERVICES</div>
          <div class="wordmark__tag">A Security Management Company</div>
        </div>
      </div>
    </header>
    <div class="photo" role="img" aria-label="Photo of a hand touching glowing digital network icons"></div>
    <svg class="stripe" viewBox="0 0 370 90" preserveAspectRatio="none" aria-hidden="true">
      <path d="M0 60 L370 10 L370 40 L0 90Z" fill="var(--blue)"/>
      <path d="M0 90 L370 40 L370 90Z" fill="var(--charcoal)"/>
    </svg>
    <h1 class="cover__title">Security Consulting and Risk Management</h1>
    <div class="cover__url">www.varnelguard.example</div>
    <p class="cover__cta">Contact us today to<br>schedule your free consultation</p>
  </article>
</section>

<!-- INSIDE SPREAD -->
<section class="spread spread--inside">

  <article class="panel services">
    <h3>Services Offered</h3>
    <ul class="list-a">
      <li>Security Management</li>
      <li>Security Management Mentoring/Development</li>
      <li>Risk Assessments</li>
      <li>Security Risk Management</li>
      <li>Security Audits</li>
      <li>Security Performance Testing (Red Team)</li>
      <li>Threat Assessments</li>
      <li>Vulnerability Assessments</li>
    </ul>
    <svg class="band" viewBox="0 0 370 30" preserveAspectRatio="none" aria-hidden="true">
      <path d="M0 30 Q185 0 370 16 L370 30Z" fill="var(--charcoal)"/>
    </svg>
    <div class="photo" role="img" aria-label="Illustration of a digital padlock and cyber security interface"></div>
    <ul class="list-b">
      <li>Security Planning</li>
      <li>RFP/RFQ</li>
      <li>Project management</li>
      <li>Security Policy Development</li>
      <li>Security Program Review</li>
      <li>Security System Design Management</li>
      <li>High Risk Planning</li>
      <li>Litigation Planning and Consulting</li>
    </ul>
  </article>

  <article class="panel consultant">
    <div class="consultant__head"></div>
    <h3>What to look for in a security consultant?</h3>
    <div class="consultant__disc" role="img" aria-label="Round photo of a business desk with laptop"></div>
    <ul>
      <li><svg viewBox="0 0 16 16" aria-hidden="true"><path d="M2 8l4 4 8-9" stroke="var(--blue)" stroke-width="2.2" fill="none"/></svg>A consultant who is Board Certified in Security management</li>
      <li><svg viewBox="0 0 16 16" aria-hidden="true"><path d="M2 8l4 4 8-9" stroke="var(--blue)" stroke-width="2.2" fill="none"/></svg>A consultant who has experience and is considered a expert in corporate security</li>
      <li><svg viewBox="0 0 16 16" aria-hidden="true"><path d="M2 8l4 4 8-9" stroke="var(--blue)" stroke-width="2.2" fill="none"/></svg>A consultant who clearly understands Business and how Security affects the bottom line</li>
      <li><svg viewBox="0 0 16 16" aria-hidden="true"><path d="M2 8l4 4 8-9" stroke="var(--blue)" stroke-width="2.2" fill="none"/></svg>A consultant who is independent who is focused on helping you address your issues.</li>
      <li><svg viewBox="0 0 16 16" aria-hidden="true"><path d="M2 8l4 4 8-9" stroke="var(--blue)" stroke-width="2.2" fill="none"/></svg>A consultant who has worked as a senior manager of a security organization</li>
    </ul>
    <div class="consultant__more">More details here<strong>www.varnelguard.example</strong></div>
  </article>

  <article class="panel expertise">
    <div class="photo" role="img" aria-label="Photo of a business team meeting around a table with laptops"></div>
    <div class="block block--areas">
      <h3>Area's of Expertise</h3>
      <ul>
        <li>Security Management</li>
        <li>Security Department Reorganization</li>
        <li>Physical Security</li>
        <li>Electronic Security</li>
        <li>Information Security</li>
        <li>Transportation Security</li>
        <li>Security in Highly Regulated environments</li>
      </ul>
    </div>
    <div class="block block--industries">
      <h3>Industries</h3>
      <ul>
        <li>Energy</li>
        <li>Healthcare</li>
        <li>Real Estate</li>
        <li>Nuclear</li>
        <li>Highly secure facilities</li>
      </ul>
    </div>
  </article>
</section>

</body>
</html>
```